Vintage soap dispenser label

I'm making a series of glass bottle soap dispensers (soap, lotion, shampoo, etc.). I really love a competitor's design, but I don't want to copy it. I'm interested in the clean, urban vintage style. There can be a lot of filler text as in their design which fills the negative space, but note that the buyer will fill the bottles with their own products, so things like "100% Natural Ingredients" and the like are somewhat bogus. Because they are to be refillable, reusable bottles, some text to that effect may be more appropriate, plus our company name "Velmora Home", and perhaps the style of the bottle "Boston Round" and other text like the size of the bottle. I need a basic design, 3.25" wide x 3.5" tall and I will adjust the text as necessary for the various products my buyers will use. My competitor that is very similar to my business is https://shoplink.example/7KpR2vX. As you can see, they have a signature style. I'd like my own signature style. (I plan to have a vintage line and a contemporary line of products, so I'll likely be posting a second request for that.)

Requirements
Should not have
• Not too ornate. Should be somewhat minimalistic

```html
<!DOCTYPE html>
<html lang="en">
<head>
<meta charset="utf-8">
<title>Velmora Home – Hand Soap Labels</title>
<link rel="stylesheet" href="https://fonts.googleapis.com/css2?family=Stardos+Stencil:wght@700&family=Source+Sans+3:wght@400&display=swap">
<style>
  :root {
    --paper: #ffffff;
    --ink: #1d1d1b;
    --rule: #2a2a2a;
    --art-light: #e4e4e4;
    --art-dark: #9a9a9a;
  }
  html, body {
    margin: 0;
    padding: 0;
    width: 1200px;
    height: 1200px;
    overflow: hidden;
    background: var(--paper);
  }
  .sheet { display: block; width: 1200px; height: 1200px; }
  .label-frame { fill: var(--paper); stroke: var(--rule); stroke-width: 2; }
  .frame-inner { fill: none; stroke: var(--rule); stroke-width: 1.2; stroke-dasharray: 3 3; }
  .rule-solid { stroke: var(--rule); stroke-width: 2; }
  .rule-dotted { stroke: var(--rule); stroke-width: 1.6; stroke-dasharray: 3 3; }
  .tag-box { fill: var(--paper); stroke: var(--rule); stroke-width: 2; }
  .tag-box-inner { fill: none; stroke: var(--rule); stroke-width: 1; }
  .display { font-family: "Stardos Stencil", Georgia, serif; font-weight: 700; fill: var(--ink); text-anchor: middle; }
  .caption { font-family: "Source Sans 3", Arial, sans-serif; font-weight: 400; fill: var(--ink); text-anchor: middle; }
  .bee-art { fill: url(#beeTone); }
</style>
</head>
<body>
<svg class="sheet" viewBox="0 0 1500 1500" xmlns="http://www.w3.org/2000/svg">
  <defs>
    <radialGradient id="beeTone" cx="50%" cy="50%" r="55%">
      <stop offset="0%" stop-color="#7d7d7d"/>
      <stop offset="60%" stop-color="#cfcfcf"/>
      <stop offset="100%" stop-color="#ffffff"/>
    </radialGradient>
  </defs>

  <!-- Label: compact -->
  <g class="label label-compact">
    <rect class="label-frame" x="135" y="66" width="458" height="620"/>
    <g class="number-tag">
      <polygon class="tag-box" points="308,88 415,88 415,94 421,94 421,127 415,127 415,133 308,133 308,127 302,127 302,94 308,94"/>
      <rect class="tag-box-inner" x="307" y="93" width="109" height="35"/>
      <text class="display" x="362" y="121" font-size="26">NO. 01</text>
    </g>
    <ellipse class="bee-art" cx="362" cy="210" rx="82" ry="58" role="img" aria-label="Vintage engraved bumblebee illustration"/>
    <line class="rule-dotted" x1="137" y1="288" x2="591" y2="288"/>
    <text class="caption" x="362" y="318" font-size="20">BOSTON ROUND BOTTLE .</text>
    <line class="rule-dotted" x1="137" y1="335" x2="591" y2="335"/>
    <line class="rule-solid" x1="137" y1="351" x2="591" y2="351"/>
    <text class="display" x="364" y="440" font-size="98" textLength="370" lengthAdjust="spacingAndGlyphs">HAND SOAP</text>
    <line class="rule-solid" x1="137" y1="460" x2="591" y2="460"/>
    <text class="caption" x="263" y="505" font-size="29">REFILLABLE</text>
    <line class="rule-solid" x1="373" y1="467" x2="373" y2="524"/>
    <text class="caption" x="472" y="503" font-size="29">REUSABLE</text>
    <line class="rule-solid" x1="137" y1="532" x2="591" y2="532"/>
    <line class="rule-dotted" x1="137" y1="549" x2="591" y2="549"/>
    <text class="display" x="362" y="580" font-size="21">VELMORA HOME .</text>
    <line class="rule-dotted" x1="137" y1="596" x2="591" y2="596"/>
    <g class="volume-tag">
      <polygon class="tag-box" points="309,620 415,620 415,625 421,625 421,661 415,661 415,666 309,666 309,661 303,661 303,625 309,625"/>
      <line class="rule-dotted" x1="306" y1="646" x2="418" y2="646"/>
      <text class="display" x="362" y="640" font-size="18">300ML</text>
      <text class="caption" x="362" y="661" font-size="10">10.14 FL OZ</text>
    </g>
  </g>

  <!-- Label: tall -->
  <g class="label label-tall">
    <rect class="label-frame" x="776" y="52" width="589" height="799"/>
    <ellipse class="bee-art" cx="1068" cy="155" rx="100" ry="72" role="img" aria-label="Vintage pencil-drawn bumblebee illustration"/>
    <line class="rule-solid" x1="778" y1="262" x2="1363" y2="262"/>
    <text class="caption" x="1068" y="299" font-size="26">BOSTON ROUND BOTTLE .</text>
    <line class="rule-dotted" x1="778" y1="320" x2="1363" y2="320"/>
    <line class="rule-solid" x1="778" y1="342" x2="1363" y2="342"/>
    <text class="display" x="1070" y="455" font-size="128" textLength="475" lengthAdjust="spacingAndGlyphs">HAND SOAP</text>
    <line class="rule-solid" x1="778" y1="483" x2="1363" y2="483"/>
    <text class="caption" x="941" y="541" font-size="38">REFILLABLE</text>
    <line class="rule-solid" x1="1082" y1="492" x2="1082" y2="565"/>
    <text class="caption" x="1210" y="538" font-size="38">REUSABLE</text>
    <line class="rule-solid" x1="778" y1="575" x2="1363" y2="575"/>
    <line class="rule-dotted" x1="778" y1="597" x2="1363" y2="597"/>
    <text class="display" x="1068" y="640" font-size="28">VELMORA HOME .</text>
    <line class="rule-dotted" x1="778" y1="658" x2="1363" y2="658"/>
    <line class="rule-solid" x1="778" y1="680" x2="1363" y2="680"/>
    <text class="display" x="996" y="742" font-size="42">300ML</text>
    <line class="rule-solid" x1="1084" y1="688" x2="1084" y2="762"/>
    <text class="caption" x="1170" y="743" font-size="22">10.14 FL OZ</text>
    <line class="rule-solid" x1="778" y1="771" x2="1363" y2="771"/>
    <text class="display" x="1083" y="822" font-size="24">NO. 01</text>
  </g>

  <!-- Label: notched corners -->
  <g class="label label-notched">
    <polygon class="label-frame" points="80,754 628,754 628,775 650,775 650,795 668,795 668,1393 650,1393 650,1412 628,1412 628,1433 80,1433 80,1412 60,1412 60,1393 40,1393 40,795 60,795 60,775 80,775"/>
    <polygon class="frame-inner" points="88,766 620,766 620,785 640,785 640,805 656,805 656,1383 640,1383 640,1402 620,1402 620,1421 88,1421 88,1402 68,1402 68,1383 52,1383 52,805 68,805 68,785 88,785"/>
    <g class="number-tag">
      <polygon class="tag-box" points="283,810 422,810 422,817 430,817 430,859 422,859 422,866 283,866 283,859 275,859 275,817 283,817"/>
      <rect class="tag-box-inner" x="281" y="816" width="143" height="44"/>
      <text class="display" x="352" y="851" font-size="34">NO. 01</text>
    </g>
    <line class="rule-dotted" x1="62" y1="893" x2="646" y2="893"/>
    <text class="caption" x="352" y="934" font-size="27">BOSTON ROUND BOTTLE .</text>
    <line class="rule-dotted" x1="62" y1="955" x2="646" y2="955"/>
    <line class="rule-solid" x1="62" y1="975" x2="646" y2="975"/>
    <text class="display" x="354" y="1088" font-size="124" textLength="480" lengthAdjust="spacingAndGlyphs">HAND SOAP</text>
    <line class="rule-solid" x1="62" y1="1118" x2="646" y2="1118"/>
    <text class="caption" x="224" y="1178" font-size="40">REFILLABLE</text>
    <line class="rule-solid" x1="367" y1="1128" x2="367" y2="1200"/>
    <text class="caption" x="495" y="1174" font-size="40">REUSABLE</text>
    <line class="rule-solid" x1="62" y1="1210" x2="646" y2="1210"/>
    <line class="rule-dotted" x1="62" y1="1230" x2="646" y2="1230"/>
    <text class="display" x="352" y="1276" font-size="28">VELMORA HOME .</text>
    <line class="rule-dotted" x1="62" y1="1295" x2="646" y2="1295"/>
    <g class="volume-tag">
      <polygon class="tag-box" points="284,1325 422,1325 422,1332 430,1332 430,1378 422,1378 422,1385 284,1385 284,1378 276,1378 276,1332 284,1332"/>
      <line class="rule-dotted" x1="280" y1="1359" x2="426" y2="1359"/>
      <text class="display" x="353" y="1352" font-size="26">300ML</text>
      <text class="caption" x="353" y="1378" font-size="13">10.14 FL OZ</text>
    </g>
  </g>
</svg>
</body>
</html>
```